Fire Hydrant Repair Parts Flyer

We need a flyer advertising both fire hydrant parts and the manufacturers that we are stocking. Our company is Coastal Flowline Supply and we are a parts distributor who sells directly to contractors. I have attached an example flyer that advertises some other parts we stock. We don't want it to look exactly like the old flyer, but we would like it to be structured similarly. I have also attached a background image for the flyer as well as some pictures of the parts we are stocking. I have also attached pictures of the manufacturer logos that we are stocking. We are trying to convey the parts that we are stocking which are: "Traffic Repair Kits", "Main Valve Repair Kits", "Extension Kits", "Replacement Caps & Gaskets", "Replacement Nozzles", Adjustable Hydrant Wrenches", "Hydrant Diffusers", & "Hydrant Oil". I have attached pictures of some of these items that we would like placed on the flyer. Let me know if you have any questions at all.

```html
<!DOCTYPE html>
<html lang="en">
<head>
<meta charset="utf-8">
<title>Fire Hydrant Parts Flyer – Coastal Flowline Supply</title>
<link rel="stylesheet" href="https://fonts.googleapis.com/css2?family=Montserrat:wght@500;600;700;800&display=swap">
<style>
  :root {
    --blue: #2549a8;
    --blue-deep: #1f3f96;
    --red: #f22b45;
    --white: #ffffff;
    --body-grey: #f2f3f5;
    --ink: #2b2b2b;
    --stage: #dcdcde;
  }
  * { margin: 0; padding: 0; box-sizing: border-box; }
  html, body { width: 1200px; height: 2566px; overflow: hidden; }
  body {
    background: var(--stage);
    font-family: "Montserrat", Arial, sans-serif;
    position: relative;
  }
  .flyer {
    position: absolute;
    left: 60px; top: 520px;
    width: 1080px; height: 1525px;
    background: var(--body-grey);
    overflow: hidden;
    box-shadow: 0 12px 30px rgba(0,0,0,.25);
  }
  .flyer-shapes { position: absolute; inset: 0; }
  .brand {
    position: absolute; left: 540px; top: 62px;
    display: flex; align-items: center; gap: 16px;
  }
  .brand-mark { width: 30px; height: 30px; border-radius: 50%; background: var(--red); }
  .brand-name { font-size: 38px; font-weight: 600; color: var(--blue); letter-spacing: -0.5px; }
  .headline {
    position: absolute; left: 115px; top: 635px; width: 850px;
    text-align: center;
  }
  .headline-title {
    font-size: 104px; font-weight: 800; color: var(--blue);
    line-height: 1; letter-spacing: 1px;
    border-bottom: 3px solid var(--red); padding-bottom: 8px;
  }
  .headline-sub {
    font-size: 41px; font-weight: 600; color: var(--red);
    line-height: 1; padding: 10px 0 6px;
    border-bottom: 3px solid var(--red);
  }
  .product {
    position: absolute; top: 815px; height: 135px;
    border-radius: 12px;
  }
  .parts-band {
    position: absolute; left: 0; top: 972px; width: 1080px; height: 217px;
    background: var(--blue);
  }
  .parts-list { position: absolute; top: 22px; list-style: none; }
  .parts-list li {
    display: flex; align-items: center; gap: 14px;
    height: 45.5px; font-size: 27px; font-weight: 500; color: var(--white);
  }
  .parts-list--left { left: 98px; }
  .parts-list--right { left: 570px; }
  .parts-divider {
    position: absolute; left: 540px; top: 34px; width: 3px; height: 160px;
    background: var(--white);
  }
  .tick { width: 20px; height: 20px; flex: none; }
  .maker-row {
    position: absolute; left: 0; width: 1080px;
    display: flex; justify-content: center; align-items: center; gap: 56px;
  }
  .maker-row--top { top: 1236px; }
  .maker-row--bottom { top: 1330px; }
  .maker {
    display: flex; align-items: center; gap: 10px;
    font-size: 22px; font-weight: 700; color: var(--ink); white-space: nowrap;
  }
  .maker-mark { width: 26px; height: 26px; flex: none; }
  .maker-mark--round { border-radius: 50%; }
  .footer-call {
    position: absolute; left: 0; top: 1440px; width: 620px;
    text-align: center; font-size: 35px; font-weight: 600; color: var(--white);
  }
  .footer-web {
    position: absolute; left: 665px; top: 1449px; width: 395px;
    display: flex; justify-content: center; align-items: center; gap: 10px;
    font-size: 26px; font-weight: 600; color: var(--white); white-space: nowrap;
  }
</style>
</head>
<body>
<main class="flyer">
  <svg class="flyer-shapes" width="1080" height="1525" viewBox="0 0 1080 1525">
    <defs>
      <linearGradient id="photoTone" x1="0" y1="0" x2="1" y2="1">
        <stop offset="0" stop-color="#6f8f4e"/>
        <stop offset="0.35" stop-color="#b8c0c4"/>
        <stop offset="0.6" stop-color="#e9eef0"/>
        <stop offset="1" stop-color="#a9b3a0"/>
      </linearGradient>
    </defs>
    <rect class="hero-photo" role="img" aria-label="Photo of a red fire hydrant on grass with a wide stream of water gushing from its nozzle" x="0" y="0" width="1080" height="620" fill="url(#photoTone)"/>
    <path class="header-panel" d="M318 0 C 430 150, 720 235, 1080 125 L1080 0 Z" fill="var(--white)"/>
    <path class="header-swoosh" d="M300 0 C 420 175, 720 262, 1080 132 L1080 122 C 720 232, 440 150, 336 0 Z" fill="var(--blue)"/>
    <path class="body-panel" d="M0 557 C 150 600, 400 625, 600 590 C 800 555, 960 420, 1080 270 L1080 1525 L0 1525 Z" fill="var(--body-grey)"/>
    <path class="red-swoosh" d="M0 494 C 200 560, 400 600, 600 570 C 800 540, 960 400, 1080 268 C 960 420, 800 555, 600 590 C 400 625, 150 600, 0 557 Z" fill="var(--red)"/>
    <polygon class="footer-red" points="0,1395 602,1395 649,1525 0,1525" fill="var(--red)"/>
    <polygon class="footer-blue" points="609,1416 1080,1416 1080,1525 657,1525" fill="var(--blue)"/>
  </svg>

  <div class="brand">
    <span class="brand-mark"></span>
    <span class="brand-name">Coastal Flowline Supply</span>
  </div>

  <header class="headline">
    <h1 class="headline-title">FIRE HYDRANT</h1>
    <p class="headline-sub">PARTS REPAIR AND MANUFACTURERS</p>
  </header>

  <div class="product" role="img" aria-label="Red hydrant cap with chain" style="left:95px;width:150px;background:linear-gradient(#e45a5a,#c9ccd0);"></div>
  <div class="product" role="img" aria-label="Adjustable hydrant wrench" style="left:283px;width:124px;background:linear-gradient(#c4c8cc,#9ea3a8);"></div>
  <div class="product" role="img" aria-label="Bottle of hydrant oil" style="left:436px;width:54px;background:linear-gradient(#f4f4f4,#c7cacd);"></div>
  <div class="product" role="img" aria-label="Traffic repair kit with coupling and bolts" style="left:549px;width:124px;background:linear-gradient(#5a5d62,#b7bcc2);"></div>
  <div class="product" role="img" aria-label="Hydrant diffuser with pressure gauge" style="left:702px;width:90px;background:linear-gradient(#f0a526,#c98618);"></div>
  <div class="product" role="img" aria-label="Hydrant extension kit" style="left:820px;width:148px;background:linear-gradient(#3d3f43,#a5aab0);"></div>

  <section class="parts-band">
    <ul class="parts-list parts-list--left">
      <li><svg class="tick" viewBox="0 0 20 20"><path d="M2 11 L8 16 L18 3" fill="none" stroke="#fff" stroke-width="3" stroke-linecap="round" stroke-linejoin="round"/></svg>Traffic Repair Kits</li>
      <li><svg class="tick" viewBox="0 0 20 20"><path d="M2 11 L8 16 L18 3" fill="none" stroke="#fff" stroke-width="3" stroke-linecap="round" stroke-linejoin="round"/></svg>Main Valve Repair Kits</li>
      <li><svg class="tick" viewBox="0 0 20 20"><path d="M2 11 L8 16 L18 3" fill="none" stroke="#fff" stroke-width="3" stroke-linecap="round" stroke-linejoin="round"/></svg>Extension Kits</li>
      <li><svg class="tick" viewBox="0 0 20 20"><path d="M2 11 L8 16 L18 3" fill="none" stroke="#fff" stroke-width="3" stroke-linecap="round" stroke-linejoin="round"/></svg>Replacement Caps &amp; Gaskets</li>
    </ul>
    <div class="parts-divider"></div>
    <ul class="parts-list parts-list--right">
      <li><svg class="tick" viewBox="0 0 20 20"><path d="M2 11 L8 16 L18 3" fill="none" stroke="#fff" stroke-width="3" stroke-linecap="round" stroke-linejoin="round"/></svg>Replacement Nozzles</li>
      <li><svg class="tick" viewBox="0 0 20 20"><path d="M2 11 L8 16 L18 3" fill="none" stroke="#fff" stroke-width="3" stroke-linecap="round" stroke-linejoin="round"/></svg>Adjustable Hydrant Wrenches</li>
      <li><svg class="tick" viewBox="0 0 20 20"><path d="M2 11 L8 16 L18 3" fill="none" stroke="#fff" stroke-width="3" stroke-linecap="round" stroke-linejoin="round"/></svg>Hydrant Diffusers</li>
      <li><svg class="tick" viewBox="0 0 20 20"><path d="M2 11 L8 16 L18 3" fill="none" stroke="#fff" stroke-width="3" stroke-linecap="round" stroke-linejoin="round"/></svg>Hydrant Oil</li>
    </ul>
  </section>

  <div class="maker-row maker-row--top">
    <div class="maker"><span class="maker-mark" style="background:var(--red)"></span>Ridgeline Pipe</div>
    <div class="maker"><span class="maker-mark maker-mark--round" style="background:#2e8b3a"></span>Harbor Valve</div>
    <div class="maker"><span class="maker-mark maker-mark--round" style="background:var(--red)"></span>Summit Flow Control</div>
  </div>
  <div class="maker-row maker-row--bottom">
    <div class="maker"><span class="maker-mark" style="background:var(--red)"></span>Keystone Hydrant</div>
    <div class="maker"><span class="maker-mark maker-mark--round" style="background:var(--red)"></span>Bayside Valve Co.</div>
    <div class="maker"><span class="maker-mark" style="background:var(--ink)"></span>Granite Valve Co.</div>
  </div>

  <p class="footer-call">Call Us Today ! : (800) 555-0142</p>
  <p class="footer-web">
    <svg width="22" height="22" viewBox="0 0 22 22" fill="none" stroke="#fff" stroke-width="1.6"><circle cx="11" cy="11" r="9"/><ellipse cx="11" cy="11" rx="4" ry="9"/><path d="M2 11 H20 M4 6 H18 M4 16 H18"/></svg>
    www.coastalflowline.com
  </p>
</main>
</body>
</html>
```